Velmorytrips.com web design project + logo design

Hi,

We are a Russian online tour operator - roamquiltex.com

We are looking to tranmsfer our domain to velmorytrips.com. The website and logo need to be velmoryesque - we are not looking to change our functionality, but we need to make the website much more attracitve to clients, much more wild looking but at the same time remaining a professional travel company.

The main concept of the website should be innovative travel (as velmory was an innovator). Alternatively, you could go down the artist route and go down the draw / design your own tour road.

On our website the customer is able to combine travel services (hotels, flights, Visa services, and soon chauffeur, car rental etc...) put it into their basket (the basket definitely has to look better than it is at the moment) and pay for it in one go by card.

We are also stressin our customer support with web chat, call centre etc... (call centre number at the top of the page)

We aim to provide an easy user experience, but we need to make it have some more style, so I will be waiting for what you guys can come up with.
Let me know if you have any questions - skype is: mrkostelin

Industry/Entity Type

It Company

Logo Text

Requirements
Must have
• It is quite a simple task - to take the existing website roamquiltex.com and velmorysize it to create velmorytrips.com, the functionality of the website will remain the same and there are not many pages in the website. Homepage, Checkout step1, Checkout step 2 (you can view both of these if you select a service) and the generic pages for T&C''s, Privacy policy etc...

IMPORTANT UPDATE

We are also looking at how the search results will look in the designs, (please do a search on our website for hotel / flight)

```html
<!DOCTYPE html>
<html lang="ru">
<head>
<meta charset="utf-8">
<title>Velmorytrips.com</title>
<link href="https://fonts.googleapis.com/css2?family=Open+Sans:wght@400;600;700&display=swap" rel="stylesheet">
<style>
:root{
  --header-bg:#2d2d2d;
  --brand-blue:#4ba3c7;
  --text-light:#ffffff;
  --text-muted:#d8d8d8;
  --text-dark:#333333;
  --field-bg:#666666;
  --field-btn:#c8c8c8;
  --search-blue:#4a8fb8;
  --panel-blue:rgba(70,120,150,.85);
  --panel-slate:rgba(60,75,85,.88);
  --panel-black:#0a0a0a;
  --footer-bg:#3e4b53;
  --footer-dark:#0c0c0c;
  --footer-cell:#2f3a40;
  --tab-active:#d4d4d4;
}
*{box-sizing:border-box;margin:0;padding:0}
html,body{width:1029px;height:1200px;overflow:hidden;background:#fff}
body{font-family:"Open Sans",Arial,sans-serif;color:var(--text-dark)}
.page{position:relative;width:1029px;height:1200px;overflow:hidden}
.abs{position:absolute}

/* header */
.site-header{left:0;top:0;width:1029px;height:94px;background:var(--header-bg)}
.brand{left:92px;top:25px;display:flex;align-items:center;gap:10px}
.brand-mark{width:44px;height:44px;border-radius:50%;border:3px solid var(--brand-blue)}
.brand-name{font-size:27px;font-weight:400;color:var(--brand-blue);letter-spacing:.5px}
.nav-item{top:42px;display:flex;align-items:center;gap:6px;font-size:11px;color:var(--text-muted);text-transform:uppercase}
.cart-select{left:835px;top:41px;width:82px;height:22px;background:#d6d6d6;color:#333;font-size:9px;display:flex;align-items:center;justify-content:center;gap:4px}

/* hero */
.hero-scene{left:0;top:94px;width:1029px;height:506px;background:linear-gradient(180deg,#4ab2e6 0%,#8fd0f0 45%,#c9c0a8 65%,#3f86b8 100%)}
.phone-panel{left:86px;top:382px;width:321px;height:114px;background:var(--panel-blue)}
.phone-main{left:26px;top:28px;font-size:29px;font-weight:700;color:#000}
.phone-alt{left:115px;top:60px;font-size:20px;color:#fff}
.hours-panel{left:86px;top:496px;width:321px;height:104px;background:var(--panel-black);color:#fff}
.hours-label{left:32px;top:16px;font-size:18px}
.hours-time{left:62px;top:40px;font-size:30px}
.pointer{left:361px;top:600px;width:0;height:0;border-left:15px solid transparent;border-right:15px solid transparent;border-top:14px solid var(--panel-black)}
.tagline-panel{left:407px;top:382px;width:510px;height:218px;background:var(--panel-slate);color:#fff;text-align:center}
.tagline-big{top:6px;width:100%;font-size:90px;line-height:1.1}
.tagline-mid{top:100px;width:100%;font-size:34px}
.tagline-low{top:124px;width:100%;font-size:62px}

/* tabs */
.tabs{left:99px;top:628px;display:flex;align-items:center;font-size:18px}
.tab{height:33px;padding:0 12px;display:flex;align-items:center}
.tab.active{background:var(--tab-active)}
.tab.empty{margin-left:28px;font-size:17px}
.tab.pay{margin-left:28px}
.rule{left:0;width:1029px;height:2px;background:linear-gradient(90deg,transparent,#ddd 20%,#ddd 80%,transparent)}
.rule.shadow{height:4px;background:linear-gradient(90deg,transparent,#bbb 20%,#bbb 80%,transparent)}

/* search form */
.label{font-size:14px;color:#444}
.field{height:33px;background:var(--field-bg);color:#e6e6e6;font-size:11px;display:flex;align-items:center;padding-left:11px}
.pax{height:31px;width:76px;background:var(--field-bg);display:flex;align-items:center;font-size:10px;color:#ddd}
.pax .drop{margin-left:auto;width:29px;height:31px;background:var(--field-btn);display:flex;align-items:center;justify-content:center}
.help{width:15px;height:15px;border-radius:50%;background:#bbb;color:#fff;font-size:10px;font-weight:700;display:flex;align-items:center;justify-content:center}
.check{display:flex;align-items:center;gap:6px;font-size:10px;color:#444}
.box{width:10px;height:10px;border:1px solid #888;background:#ccc}
.box.on{background:#fff;box-shadow:inset 0 0 0 2px #fff,inset 0 0 0 5px #666}
.search-btn{left:597px;top:849px;width:242px;height:32px;background:var(--search-blue);color:#fff;font-size:15px;display:flex;align-items:center;justify-content:center;gap:6px}

/* footer */
.site-footer{left:0;top:1010px;width:1029px;height:190px;background:var(--footer-bg)}
.foot-col{top:33px;color:#fff}
.foot-col h3{font-size:14px;font-weight:400;margin-bottom:15px}
.foot-col li{list-style:none;font-size:11px;line-height:14.5px}
.foot-brand{left:455px;top:0;width:476px;height:190px;background:var(--footer-dark)}
.foot-logo{right:10px;top:16px;display:flex;align-items:center;gap:8px}
.foot-logo .brand-mark{width:36px;height:36px}
.foot-logo .brand-name{font-size:23px}
.social{top:56px;width:31px;height:31px;border-radius:50%;background:#fff}
.contact-cell{top:134px;height:56px;color:#fff;font-size:12px;display:flex;align-items:center;justify-content:center;text-align:center}
.contact-icon{top:114px;width:32px;height:32px;border-radius:50%;border:2px solid #fff;background:#111;display:flex;align-items:center;justify-content:center}
</style>
</head>
<body>
<div class="page">

  <header class="site-header abs">
    <div class="brand abs">
      <span class="brand-mark"></span>
      <span class="brand-name">VELMORYTRAVEL</span>
    </div>
    <div class="nav-item abs" style="left:464px">
      <svg width="16" height="16" viewBox="0 0 16 16"><rect x="1" y="3" width="11" height="11" fill="none" stroke="#ccc" stroke-width="1.5"/><path d="M7 9l7-7" stroke="#ccc" stroke-width="2"/></svg>Форум
    </div>
    <div class="nav-item abs" style="left:586px">
      <svg width="16" height="10" viewBox="0 0 16 10"><rect width="16" height="3.3" fill="#eee"/><rect y="3.3" width="16" height="3.3" fill="#aaa"/><rect y="6.6" width="16" height="3.4" fill="#888"/></svg>Язык
    </div>
    <div class="nav-item abs" style="left:692px">
      <svg width="18" height="16" viewBox="0 0 18 16"><path d="M1 3l5-2 6 2 5-2v12l-5 2-6-2-5 2z" fill="none" stroke="#ccc" stroke-width="1.5"/></svg>Мой тур
    </div>
    <svg class="abs" style="left:808px;top:42px" width="22" height="20" viewBox="0 0 22 20"><path d="M1 2h4l3 11h10l3-8H7" fill="none" stroke="#ccc" stroke-width="1.8"/><circle cx="9" cy="17" r="1.8" fill="#ccc"/><circle cx="17" cy="17" r="1.8" fill="#ccc"/></svg>
    <div class="cart-select abs">КОРЗИНА (0) <svg width="8" height="5"><path d="M0 0h8L4 5z" fill="#333"/></svg></div>
  </header>

  <div class="hero-scene abs" role="img" aria-label="Коллаж мировых достопримечательностей на фоне неба с самолётами и воздушными шарами"></div>

  <div class="phone-panel abs">
    <div class="phone-main abs">8-800-555-0142</div>
    <div class="phone-alt abs">+7 (495) 555-01-87</div>
  </div>
  <div class="hours-panel abs">
    <div class="hours-label abs">(Пн-Пт) Часы работы</div>
    <div class="hours-time abs">с 9:00 - до 18:00</div>
  </div>
  <div class="pointer abs"></div>
  <div class="tagline-panel abs">
    <div class="tagline-big abs">Больше</div>
    <div class="tagline-mid abs" style="top:100px">чем опыт</div>
    <div class="tagline-low abs" style="top:120px">путешествия</div>
  </div>

  <nav class="tabs abs">
    <span class="tab active">Корзина</span>
    <span class="tab empty">пусто</span>
    <span class="tab pay">Оплата</span>
  </nav>
  <div class="rule abs" style="top:662px"></div>

  <form class="search-form">
    <span class="label abs" style="left:112px;top:700px">Откуда</span>
    <div class="field abs" style="left:216px;top:693px;width:279px">Город</div>
    <span class="label abs" style="left:539px;top:700px">Куда</span>
    <div class="field abs" style="left:600px;top:693px;width:239px">Город</div>

    <span class="label abs" style="left:112px;top:752px">Туда</span>
    <div class="field abs" style="left:216px;top:742px;width:281px;padding-left:4px;gap:12px">
      <svg width="24" height="24" viewBox="0 0 24 24"><rect x="2" y="4" width="20" height="18" fill="#ddd"/><rect x="2" y="4" width="20" height="5" fill="#999"/><text x="12" y="20" font-size="11" text-anchor="middle" fill="#555" font-family="Arial,sans-serif" font-weight="700">7</text></svg>(16-6-2013)
    </div>
    <span class="label abs" style="left:536px;top:750px">Обратно</span>
    <div class="field abs" style="left:600px;top:746px;width:239px;padding-left:7px">(Обратно)</div>

    <span class="label abs" style="left:112px;top:805px">Пассажиры</span>
    <div class="pax abs" style="left:216px;top:793px"><span style="padding-left:22px">(1)</span><span class="drop"><svg width="10" height="6"><path d="M0 0h10L5 6z" fill="#444"/></svg></span></div>
    <span class="help abs" style="left:297px;top:799px">?</span>
    <div class="pax abs" style="left:318px;top:793px"><span style="padding-left:22px">(0)</span><span class="drop"><svg width="10" height="6"><path d="M0 0h10L5 6z" fill="#444"/></svg></span></div>
    <span class="help abs" style="left:399px;top:799px">?</span>
    <div class="pax abs" style="left:420px;top:793px"><span style="padding-left:22px">(0)</span><span class="drop"><svg width="10" height="6"><path d="M0 0h10L5 6z" fill="#444"/></svg></span></div>
    <span class="help abs" style="left:501px;top:799px">?</span>

    <div class="check abs" style="left:601px;top:797px"><span class="box"></span>Обратно</div>
    <div class="check abs" style="left:601px;top:814px"><span class="box on"></span>В одну сторону</div>

    <span class="label abs" style="left:112px;top:857px">Класс</span>
    <div class="field abs" style="left:215px;top:848px;width:281px;padding-right:0">Эконом<span style="margin-left:auto;width:29px;height:33px;background:var(--field-btn);display:flex;align-items:center;justify-content:center"><svg width="10" height="6"><path d="M0 0h10L5 6z" fill="#444"/></svg></span></div>

    <div class="search-btn abs">
      <svg width="17" height="17" viewBox="0 0 17 17"><circle cx="7" cy="7" r="5" fill="none" stroke="#fff" stroke-width="2.5"/><path d="M11 11l5 5" stroke="#fff" stroke-width="3"/></svg>Поиск
    </div>
  </form>
  <div class="rule shadow abs" style="top:934px"></div>

  <footer class="site-footer abs">
    <div class="foot-col abs" style="left:113px">
      <h3>Просмотр Сайта</h3>
      <ul><li>Домой</li><li>О нас</li><li>Форум</li><li>Контакты</li><li>Помощь</li></ul>
    </div>
    <div class="foot-col abs" style="left:308px;width:90px">
      <h3>Помощь</h3>
      <ul><li>Помощь</li><li>Правила пользования</li><li>Политика конфиденциальности</li><li>Cookies</li></ul>
    </div>
    <div class="foot-brand abs">
      <div class="foot-logo abs"><span class="brand-mark"></span><span class="brand-name">VELMORYTRAVEL</span></div>
      <span class="social abs" style="left:352px"></span>
      <span class="social abs" style="left:391px"></span>
      <span class="social abs" style="left:430px"></span>
      <div class="contact-cell abs" style="left:0;width:158px;background:var(--footer-cell);justify-content:flex-start;padding-left:30px;text-align:left;font-size:11px">14 Harlow Lane<br>London, E2 7QX,UK</div>
      <div class="contact-cell abs" style="left:158px;width:160px;background:#36444b">+7 (495) 555-01-87</div>
      <div class="contact-cell abs" style="left:318px;width:158px;background:var(--footer-cell)">info@roamquiltex.com</div>
      <span class="contact-icon abs" style="left:61px"><svg width="14" height="18" viewBox="0 0 14 18"><path d="M7 17C3 11 1 8 1 6a6 6 0 0112 0c0 2-2 5-6 11z" fill="none" stroke="#fff" stroke-width="1.6"/><circle cx="7" cy="6" r="2" fill="#fff"/></svg></span>
      <span class="contact-icon abs" style="left:222px"><svg width="12" height="18" viewBox="0 0 12 18"><rect x="1" y="1" width="10" height="16" rx="2" fill="none" stroke="#fff" stroke-width="1.6"/><circle cx="6" cy="14" r="1" fill="#fff"/></svg></span>
      <span class="contact-icon abs" style="left:381px"><svg width="18" height="13" viewBox="0 0 18 13"><rect x="1" y="1" width="16" height="11" fill="none" stroke="#fff" stroke-width="1.6"/><path d="M1 1l8 6 8-6" fill="none" stroke="#fff" stroke-width="1.6"/></svg></span>
    </div>
  </footer>

</div>
</body>
</html>
```